Website 950x200 Header w/ logo

I'm in need of a website header for a new site called TalesofGordo.com

The site is basically a glorified blog for myself to write my thoughts about politics, sports, TV shows, current events, whatever. I have a lot of interests.

The site is going to look very very similar to http://www.quillpostmedia.com/5930417/7-tips-for-hiring-bold-minds

but instead of having a dynamic header that becomes the picture with each article, its just going to be a static header in which I'd like to have the name of the site (Tales of Gordo) and some kind of logo, pictures, etc - I'm totally open to anything. The only thing is it needs to have a dark (probably black) background and needs to be 950x200px.

I envision a black background, with gray and white as the primary colors and then some secondary colors potentially, but again I'm open to anything as long as it's on the black background or some kind of charcoal gray or wahtever. On the site the black part will go all the way from the left of the screen to the right no matter what the window size, but I'd like to keep all the content inside of 950x200px

email me gordo.pellwick@zentramail.com if you have any questions. Thanks!

```html
<!DOCTYPE html>
<html lang="en">
<head>
<meta charset="utf-8">
<title>Tales of Gordo</title>
<link href="https://fonts.googleapis.com/css2?family=Cinzel:wght@700&display=swap" rel="stylesheet">
<style>
  :root {
    --ink: #000000;
    --charcoal: #2e2e2e;
    --smoke: #1c1c1c;
    --grass: #0a0a0a;
    --title: #ffffff;
  }
  html, body {
    margin: 0;
    padding: 0;
    width: 1200px;
    height: 253px;
    overflow: hidden;
    background: var(--ink);
  }
  .site-header {
    position: relative;
    width: 1200px;
    height: 253px;
    background: var(--ink);
    overflow: hidden;
  }
  .header-scene {
    position: absolute;
    inset: 0;
    background:
      linear-gradient(90deg, transparent 0%, transparent 78%, var(--smoke) 82%, var(--charcoal) 100%) 0 60px / 100% 60px no-repeat,
      linear-gradient(180deg,
        var(--charcoal) 0%,
        var(--smoke) 14%,
        var(--grass) 24%,
        var(--ink) 55%,
        var(--ink) 100%);
  }
  .site-title {
    position: absolute;
    left: 14px;
    top: 112px;
    margin: 0;
    font-family: "Cinzel", serif;
    font-weight: 700;
    font-size: 108px;
    line-height: 1;
    letter-spacing: 2px;
    color: var(--title);
    white-space: nowrap;
  }
</style>
</head>
<body>
  <header class="site-header">
    <div class="header-scene" role="img" aria-label="Grey brush-stroke sky over a dark silhouette of tall grass and treeline"></div>
    <h1 class="site-title">Tales of Gordo</h1>
  </header>
</body>
</html>
```